TK Workshop - flyer

We are a machine shop. While making sales calls in the field, we need a flyer to leave behind with prospect to attract interest.

Target Market(s)

Medical device, aerospace and aviation component manfacturers

Font styles to use
Serif

Colors

Designer to choose colors to be used in the design.

Requirements
Must have
• NA
Nice to have
• NA
Should not have
• NA

```html
<!DOCTYPE html>
<html lang="en">
<head>
<meta charset="utf-8">
<title>TK Workshop – Flyer</title>
<link rel="stylesheet" href="https://fonts.googleapis.com/css2?family=Cinzel:wght@600;700&family=Lato:wght@400;700;900&display=swap">
<style>
  :root {
    --navy: #1d5785;
    --navy-dark: #163f63;
    --red: #e41e26;
    --ink: #2a2a2a;
    --paper: #ffffff;
    --backdrop: #e4e5e7;
  }
  * { box-sizing: border-box; margin: 0; padding: 0; }
  html, body { width: 1200px; height: 1200px; overflow: hidden; }
  body { background: var(--backdrop); font-family: "Lato", sans-serif; color: var(--ink); }

  .flyer {
    position: absolute; left: 200px; top: 35px;
    width: 800px; height: 1130px;
    background: var(--paper);
    overflow: hidden;
    box-shadow: 0 6px 24px rgba(0,0,0,.18);
  }
  .flyer-shapes { position: absolute; inset: 0; }

  .shop-photo {
    position: absolute; inset: 0;
    clip-path: polygon(0 0, 300px 0, 345px 115px, 520px 115px, 560px 360px, 400px 440px, 0 470px);
    background: linear-gradient(160deg, #cfcfcf 0%, #8e8e8e 45%, #5c5c5c 80%, #9a9a9a 100%);
  }
  .product-photo {
    position: absolute;
    background: radial-gradient(ellipse at center, #e6ecea 0%, #f3f5f4 60%, #ffffff 100%);
  }
  .product-photo--main { left: 520px; top: 360px; width: 260px; height: 330px; }
  .product-photo--lower { left: 40px; top: 790px; width: 380px; height: 30px; }

  .brand {
    position: absolute; left: 330px; top: 28px; width: 440px;
    display: flex; flex-direction: column; align-items: center;
  }
  .brand-name {
    display: flex; align-items: center; gap: 12px;
    font-family: "Lato", sans-serif; font-weight: 700; font-size: 44px;
    color: var(--navy-dark); letter-spacing: -0.5px;
  }
  .brand-dot { width: 26px; height: 26px; border-radius: 50%; background: var(--red); }
  .brand-tagline {
    margin-top: 2px; font-size: 11px; letter-spacing: 2.5px; color: var(--navy);
  }

  .sectors {
    position: absolute; left: 400px; top: 130px; width: 380px;
    color: #fff; font-weight: 700; font-size: 15px; line-height: 30px; text-align: center;
  }
  .sectors .sep { margin: 0 8px; opacity: .8; }

  .services {
    position: absolute; left: 50px; top: 500px; color: #fff;
  }
  .services-title {
    font-family: "Cinzel", serif; font-weight: 700; font-size: 26px; letter-spacing: 3px;
    margin-bottom: 12px;
  }
  .services-list { list-style: none; }
  .services-list li {
    display: flex; align-items: center; gap: 12px;
    font-weight: 700; font-size: 18px; line-height: 34px;
  }
  .tick { width: 18px; height: 18px; flex: none; }

  .facilities {
    position: absolute; left: 480px; top: 700px; width: 300px; list-style: none;
    font-weight: 900; font-size: 14px; color: #222;
  }
  .facilities li { display: flex; gap: 10px; margin-bottom: 14px; line-height: 18px; }
  .facilities .tick { margin-top: 1px; }

  .intro {
    position: absolute; left: 40px; top: 835px; width: 520px;
    font-size: 18px; line-height: 24px; color: #333;
  }

  .contact {
    position: absolute; left: 40px; top: 1000px; color: #fff;
  }
  .contact-call { font-weight: 900; font-size: 28px; letter-spacing: .5px; }
  .contact-call .phone { font-size: 34px; margin-left: 6px; }
  .contact-line { font-weight: 700; font-size: 16px; margin-top: 6px; }
</style>
</head>
<body>
  <main class="flyer">
    <div class="shop-photo" role="img" aria-label="Black and white photo of a hydraulic press in the machine shop"></div>

    <svg class="flyer-shapes" width="800" height="1130" viewBox="0 0 800 1130" aria-hidden="true">
      <polygon class="sector-band" points="345,115 800,85 800,245 700,330 548,350 520,300" fill="var(--navy)"/>
      <polygon class="accent-wedge" points="478,330 565,440 430,575" fill="var(--red)"/>
      <polygon class="services-panel" points="0,470 520,420 460,740 0,775" fill="var(--navy)"/>
      <polygon class="footer-stripe" points="600,925 800,895 800,907 620,935" fill="var(--navy)"/>
      <polygon class="footer-stripe" points="650,942 800,918 800,932 675,950" fill="var(--navy)"/>
      <polygon class="footer-band" points="0,990 800,940 800,1130 0,1130" fill="var(--red)"/>
    </svg>

    <div class="product-photo product-photo--main" role="img" aria-label="Machined medical implant parts: anodized screw heads, pedicle screws and blue rings"></div>
    <div class="product-photo product-photo--lower" role="img" aria-label="Anodized green and purple pedicle screws"></div>

    <header class="brand">
      <div class="brand-name">TK Workshop <span class="brand-dot"></span></div>
      <div class="brand-tagline">High Quality doesn't mean high cost</div>
    </header>

    <div class="sectors">
      <div>Medical<span class="sep">|</span>Implants<span class="sep">|</span>Aerospace</div>
      <div>Aviation<span class="sep">|</span>Military applications</div>
      <div>ISO 13485<span class="sep">|</span>9100<span class="sep">|</span>9001 certified</div>
    </div>

    <section class="services">
      <h2 class="services-title">Our Services</h2>
      <ul class="services-list">
        <li><svg class="tick" viewBox="0 0 20 20"><circle cx="10" cy="10" r="8.5" fill="none" stroke="#fff" stroke-width="2"/><path d="M6 10.3l2.6 2.6L14 7.5" fill="none" stroke="#fff" stroke-width="2"/></svg>5 Axis Cnc Milling</li>
        <li><svg class="tick" viewBox="0 0 20 20"><circle cx="10" cy="10" r="8.5" fill="none" stroke="#fff" stroke-width="2"/><path d="M6 10.3l2.6 2.6L14 7.5" fill="none" stroke="#fff" stroke-width="2"/></svg>Turning</li>
        <li><svg class="tick" viewBox="0 0 20 20"><circle cx="10" cy="10" r="8.5" fill="none" stroke="#fff" stroke-width="2"/><path d="M6 10.3l2.6 2.6L14 7.5" fill="none" stroke="#fff" stroke-width="2"/></svg>Cnc Swiss-type</li>
        <li><svg class="tick" viewBox="0 0 20 20"><circle cx="10" cy="10" r="8.5" fill="none" stroke="#fff" stroke-width="2"/><path d="M6 10.3l2.6 2.6L14 7.5" fill="none" stroke="#fff" stroke-width="2"/></svg>Deburring</li>
        <li><svg class="tick" viewBox="0 0 20 20"><circle cx="10" cy="10" r="8.5" fill="none" stroke="#fff" stroke-width="2"/><path d="M6 10.3l2.6 2.6L14 7.5" fill="none" stroke="#fff" stroke-width="2"/></svg>Laser Marking</li>
        <li><svg class="tick" viewBox="0 0 20 20"><circle cx="10" cy="10" r="8.5" fill="none" stroke="#fff" stroke-width="2"/><path d="M6 10.3l2.6 2.6L14 7.5" fill="none" stroke="#fff" stroke-width="2"/></svg>Optiscan Vision 302</li>
      </ul>
    </section>

    <ul class="facilities">
      <li><svg class="tick" viewBox="0 0 20 20"><circle cx="10" cy="10" r="8.5" fill="none" stroke="var(--navy)" stroke-width="2"/><path d="M6 10.3l2.6 2.6L14 7.5" fill="none" stroke="var(--navy)" stroke-width="2"/></svg>Coordinate measuring machines, comparators, surface plated micrometers</li>
      <li><svg class="tick" viewBox="0 0 20 20"><circle cx="10" cy="10" r="8.5" fill="none" stroke="var(--navy)" stroke-width="2"/><path d="M6 10.3l2.6 2.6L14 7.5" fill="none" stroke="var(--navy)" stroke-width="2"/></svg>Dedicated temperature controlled room</li>
      <li><svg class="tick" viewBox="0 0 20 20"><circle cx="10" cy="10" r="8.5" fill="none" stroke="var(--navy)" stroke-width="2"/><path d="M6 10.3l2.6 2.6L14 7.5" fill="none" stroke="var(--navy)" stroke-width="2"/></svg>Ultrasonic cleaning &amp; reverse osmosis water</li>
    </ul>

    <p class="intro">Our Education, Training, and 25 years of Medical and Aerospace machining experience helps us determine the best possible methods of manufacture that will be most cost effective for your parts.</p>

    <footer class="contact">
      <div class="contact-call">CALL US NOW:<span class="phone">(555) 014-2280</span></div>
      <div class="contact-line">4120 Linden Street, Unit B, Maple Ridge, CA 90000</div>
      <div class="contact-line">www.tkworkshopcnc.com</div>
    </footer>
  </main>
</body>
</html>
```